Business Card Design

My business will be called TB Joinery & Renovations. I am a liscenced carpentar who specialises in renovations/alterations/refurbishments and maintenance. I have experience in all types of Carpentry tho. I also have experience in tiling, painting and concrete which obviously gives me an edge in the refurbishment market for building. But i am not liscenced in these trades. I pride myself on being an honest and very reliable. There are alot of tradesman where i live who are not reliable so i really want to let the community know they can trust me and that i am willing to do all types of work.
I would like to see design and is not over the top but uses earthy/modern colours which presents a down to earth message.

I would really like to communicate diversity, reliabilty and quality work.

I have attached a couple of concepts i have come up with PaperKite, These may aid you.

Industry/Entity Type

Painting

Contact Information for Business Card

Name: Dean Wolworth
Email: dean.wolw@postlark.net
Ph: 0418529364

Requirements
Must have
• Licence No: 318827K

```html
<!DOCTYPE html>
<html lang="en">
<head>
<meta charset="utf-8">
<title>TB Joinery &amp; Renovations – Business Card</title>
<link rel="stylesheet" href="https://fonts.googleapis.com/css2?family=Roboto:wght@700;900&family=Michroma&display=swap">
<style>
  :root {
    --page-bg: #ecebe8;
    --card-white: #f4f4f4;
    --ink-dark: #3a3a3d;
    --steel-dark: #5b5b60;
    --steel-mid: #8d8d96;
    --steel-light: #cfcfdc;
    --rule-dark: #2f2f33;
    --accent-yellow: #f3e000;
    --accent-yellow-deep: #c9b800;
    --text-light: #ffffff;
  }
  * { margin: 0; padding: 0; box-sizing: border-box; }
  html, body {
    width: 1132px; height: 1200px; overflow: hidden;
    background: var(--page-bg);
  }
  .canvas { position: relative; width: 1132px; height: 1200px; }

  .card {
    position: absolute; left: 86px; width: 960px;
    border-radius: 30px; overflow: hidden;
    box-shadow: 0 4px 14px rgba(0,0,0,.18);
  }
  .steel {
    background:
      linear-gradient(180deg, rgba(255,255,255,.06), rgba(0,0,0,.12)),
      linear-gradient(90deg, var(--steel-dark) 0%, var(--steel-mid) 35%, var(--steel-light) 58%, var(--steel-mid) 80%, var(--steel-dark) 100%);
  }

  /* Front */
  .card-front { top: 33px; height: 546px; }
  .front-top {
    position: absolute; left: 0; top: 0; width: 100%; height: 250px;
    background: linear-gradient(180deg, #ffffff, var(--card-white) 70%, #e3e3e3);
  }
  .front-rule { position: absolute; left: 0; top: 250px; width: 100%; height: 6px; background: var(--rule-dark); }
  .front-body { position: absolute; left: 0; top: 256px; width: 100%; height: 290px; }

  .brand-name {
    position: absolute; font-family: "Roboto", sans-serif; font-weight: 900;
    color: var(--ink-dark); text-align: center; letter-spacing: -1px; line-height: 1.05;
  }
  .card-front .brand-name { left: 0; width: 100%; top: 70px; font-size: 56px; }

  .tab { position: absolute; }
  .tab svg { position: absolute; left: 0; top: 0; width: 100%; height: 100%; }
  .name-tab { left: 500px; top: 262px; width: 460px; height: 92px; }
  .holder-name {
    position: absolute; left: 80px; top: 0; line-height: 92px;
    font-family: "Roboto", sans-serif; font-weight: 700; font-size: 27px; color: var(--ink-dark);
  }

  .services {
    position: absolute; left: 36px; top: 432px; list-style: none;
    font-family: "Michroma", sans-serif; font-size: 13.5px; color: var(--text-light);
    letter-spacing: 1.6px; line-height: 24px;
  }
  .contact {
    position: absolute; right: 30px; top: 456px; list-style: none; text-align: right;
    font-family: "Michroma", sans-serif; font-size: 16px; color: var(--text-light);
    letter-spacing: 1.4px; line-height: 23px;
  }
  .contact .dot {
    display: inline-block; width: 9px; height: 9px; margin-left: 3px; border-radius: 50%;
    background: var(--accent-yellow); vertical-align: middle;
  }

  /* Back */
  .card-back { top: 623px; height: 550px; }
  .card-back .brand-name { left: 0; width: 100%; top: 145px; font-size: 92px; }
  .email-tab { left: 500px; top: 454px; width: 460px; height: 80px; }
  .email-tab .email {
    position: absolute; left: 70px; top: 0; line-height: 80px;
    font-family: "Michroma", sans-serif; font-size: 18px; color: var(--ink-dark); letter-spacing: 1.4px;
  }
</style>
</head>
<body>
<main class="canvas">

  <section class="card card-front" aria-label="Business card front">
    <div class="front-top"></div>
    <div class="front-rule"></div>
    <div class="front-body steel"></div>

    <h1 class="brand-name">TB Joinery &amp; Renovations</h1>

    <div class="tab name-tab">
      <svg viewBox="0 0 460 92" preserveAspectRatio="none" aria-hidden="true">
        <defs>
          <linearGradient id="tabFillFront" x1="0" x2="1" y1="0" y2="0">
            <stop offset="0" stop-color="var(--accent-yellow-deep)"/>
            <stop offset="0.25" stop-color="var(--accent-yellow)"/>
            <stop offset="1" stop-color="var(--accent-yellow)"/>
          </linearGradient>
        </defs>
        <path d="M0 0 H360 Q412 0 412 46 Q412 92 380 92 H40 Q22 92 16 72 Z" fill="url(#tabFillFront)"/>
      </svg>
      <span class="holder-name">Dean Wolworth</span>
    </div>

    <ul class="services">
      <li>Carpentry &amp; All Building Services</li>
      <li>Renovations</li>
      <li>Maintenance</li>
      <li>General Repairs</li>
    </ul>

    <ul class="contact">
      <li>Licence No: 318827K</li>
      <li>0418529364<span class="dot"></span></li>
      <li>dean.wolw@postlark.net<span class="dot"></span></li>
    </ul>
  </section>

  <section class="card card-back steel" aria-label="Business card back">
    <h2 class="brand-name">TB Joinery<br>&amp; Renovations</h2>

    <div class="tab email-tab">
      <svg viewBox="0 0 460 80" preserveAspectRatio="none" aria-hidden="true">
        <defs>
          <linearGradient id="tabFillBack" x1="0" x2="1" y1="0" y2="0">
            <stop offset="0" stop-color="var(--accent-yellow-deep)"/>
            <stop offset="0.25" stop-color="var(--accent-yellow)"/>
            <stop offset="1" stop-color="var(--accent-yellow)"/>
          </linearGradient>
        </defs>
        <path d="M22 0 H400 Q440 0 440 40 Q440 80 400 80 H0 V60 Q4 0 22 0 Z" fill="url(#tabFillBack)"/>
      </svg>
      <span class="email">dean.wolw@postlark.net</span>
    </div>
  </section>

</main>
</body>
</html>
```